Kestrel Dune Pictures Original Content TV Series & Reality TV, TV Commercials Movies Film Production

Hello Website revamp please. Would like a contemporary, simple, graphic, clean design, easy to navigate that highlights our skills in a remarkable design - might have to consider 2 sites, one that displays our long standing experience in film production service business, where we facilitate international film makers in SA. A second site that displays our work in development- where we create and conceptualise our own films and TV shows for the global market. Please see www.kdpictures.co.za for current website. Would like to retain the current red logo.

Target Market(s)

Film Studios

Coding

Number of Pages Required

2 page

Font styles to use
Sans Serif

Colors
ec1f27

Requirements
Must have
• Its own style
Nice to have
• Its own style
Should not have
• Template feeling to it

```html
<!DOCTYPE html>
<html lang="en">
<head>
<meta charset="utf-8">
<title>Kestrel Dune Pictures</title>
<link rel="stylesheet" href="https://fonts.googleapis.com/css2?family=Oswald:wght@400;500;600&family=Open+Sans:wght@400;600&display=swap">
<style>
:root{
  --red:#ec1f27;
  --red-deep:#c3121a;
  --ink:#111111;
  --charcoal:#2b2b2d;
  --text:#555555;
  --muted:#8a8a8a;
  --paper:#ffffff;
  --mist:#e4e4e4;
}
*{margin:0;padding:0;box-sizing:border-box}
html,body{width:1200px;height:4706px;overflow:hidden;background:var(--paper)}
body{font-family:"Open Sans",Arial,sans-serif;color:var(--text)}
.canvas{position:relative;width:1200px;height:4706px;overflow:hidden}
.block{position:absolute;left:0;width:1200px}
.heading{font-family:"Oswald",Arial,sans-serif;font-weight:400;font-size:34px;color:var(--ink);text-align:center;text-transform:uppercase;letter-spacing:-.5px}
.heading em{font-style:normal;color:var(--red)}
.rule{display:block;width:120px;height:3px;background:var(--red);margin:14px auto 0}
.btn{display:inline-block;font-family:"Oswald",Arial,sans-serif;font-weight:500;font-size:16px;text-transform:uppercase;text-decoration:none;text-align:center;width:155px;height:50px;line-height:50px;border-radius:4px}
.btn-red{background:var(--red);color:#fff}
.btn-white{background:#fff;color:var(--ink)}

/* header */
.site-header{top:0;height:102px;background:#fff}
.brand{position:absolute;left:113px;top:33px;display:flex;align-items:center;gap:10px;font-family:"Oswald",Arial,sans-serif;font-weight:600;font-size:19px;color:var(--red);text-transform:uppercase;text-decoration:none}
.brand-dot{width:30px;height:30px;border-radius:50%;background:var(--red)}
.nav a{position:absolute;top:48px;font-family:"Oswald",Arial,sans-serif;font-weight:500;font-size:13px;color:var(--ink);text-decoration:none;text-transform:uppercase}
.nav a.active{color:var(--red)}
.call{position:absolute;left:880px;top:31px;display:flex;align-items:center;gap:12px}
.call-icon{width:50px;height:50px;border-radius:50%;background:var(--red);display:flex;align-items:center;justify-content:center}
.call small{display:block;font-size:11px;color:var(--red)}
.call strong{display:block;font-family:"Oswald",Arial,sans-serif;font-weight:500;font-size:21px;color:var(--ink);line-height:1.1}

/* hero */
.hero{top:102px;height:638px}
.hero-photo{position:absolute;inset:0;background:radial-gradient(ellipse at 55% 10%,#6d6a64 0%,#3a3835 30%,#151413 65%,#050505 100%)}
.hero-cut{position:absolute;left:0;top:0}
.hero-title{position:absolute;top:196px;width:100%;text-align:center;font-family:"Oswald",Arial,sans-serif;font-weight:500;font-size:54px;color:#fff;text-transform:uppercase}
.hero-lead{position:absolute;top:280px;width:100%;text-align:center;font-size:15px;line-height:30px;color:#fff}
.hero .btn{position:absolute;left:523px;top:377px;height:49px;line-height:49px}
.slide-nav{position:absolute;top:260px;width:14px;font-family:"Oswald",Arial,sans-serif;font-size:12px;color:#fff;text-align:center;line-height:33px}
.slide-nav.prev{left:42px}
.slide-nav.next{left:1144px}

/* about */
.about{top:740px;height:456px;text-align:center}
.about .heading{margin-top:80px}
.about p{width:900px;margin:30px auto 0;font-size:14px;line-height:30px;color:var(--text)}
.about .btn{margin-top:34px}

/* services split */
.services{top:1196px;height:494px}
.services svg{position:absolute;left:0;top:0}
.service{position:absolute;top:127px;width:430px;color:#fff}
.service h3{font-family:"Oswald",Arial,sans-serif;font-weight:500;font-size:25px;line-height:32px;text-transform:uppercase}
.service p{margin-top:10px;font-size:15px;line-height:32px}
.service .btn{margin-top:20px}
.service.production{left:113px;top:127px}
.service.production h3{margin-top:0}
.service.development{left:660px;top:120px}

/* what we do */
.what{top:1690px;height:603px}
.what .heading{margin-top:88px}
.step-num{position:absolute;font-family:"Oswald",Arial,sans-serif;font-weight:600;color:#000;line-height:1}
.step{position:absolute;width:248px;height:248px;border-radius:50%;background:#fff;box-shadow:8px 10px 14px rgba(0,0,0,.28)}
.step h4{position:absolute;font-family:"Oswald",Arial,sans-serif;font-weight:500;font-size:25px;color:#000}
.step p{position:absolute;font-size:13px;line-height:30px;color:var(--muted);width:175px}
.step svg{position:absolute}
.step-arrow{position:absolute;width:42px;height:42px;border-radius:50%;background:var(--red);display:flex;align-items:center;justify-content:center}

/* latest shows */
.shows{top:2293px;height:831px}
.shows>svg{position:absolute;left:0;top:0}
.shows .heading{position:absolute;top:172px;width:100%;color:#fff;font-size:33px}
.shows .rule{background:#fff;width:215px}
.show{position:absolute;top:283px;width:230px;text-align:center;color:#fff}
.poster{display:block;width:230px;height:285px}
.show h5{margin-top:14px;font-family:"Oswald",Arial,sans-serif;font-weight:400;font-size:20px;text-transform:uppercase}
.show span{display:block;font-size:13px;margin-top:2px}
.dots{position:absolute;top:683px;left:570px;display:flex;gap:4px}
.dots i{width:11px;height:11px;border-radius:50%;background:#fff}
.dots i.off{background:transparent;border:2px solid #fff}

/* testimonials */
.testimonials{top:3124px;height:503px;background:var(--mist);text-align:center}
.testimonials .heading{margin-top:92px}
.quote-mark{display:block;margin:38px auto 0;font-family:"Oswald",Arial,sans-serif;font-size:56px;line-height:30px;color:var(--red);font-style:italic;height:30px}
.testimonials p{width:820px;margin:14px auto 0;font-size:14px;line-height:30px;color:var(--muted)}
.reviewer{display:flex;align-items:center;justify-content:center;gap:20px;margin-top:20px}
.avatar{width:56px;height:56px;border-radius:50%;background:radial-gradient(circle at 50% 40%,#b8b2ad,#4a4644)}
.reviewer span{font-family:"Oswald",Arial,sans-serif;font-size:15px;color:var(--red);text-transform:uppercase}

/* blogs */
.blogs{top:3627px;height:621px}
.blogs .heading{margin-top:92px}
.post{position:absolute;top:186px;width:314px}
.post-photo{display:block;width:314px;height:203px;border-radius:6px}
.post h6{padding:0 15px;margin-top:20px;font-family:"Oswald",Arial,sans-serif;font-weight:400;font-size:20px;line-height:29px;color:var(--ink)}
.post p{padding:0 15px;margin-top:18px;font-size:13px;line-height:30px;color:var(--muted)}

/* footer */
.site-footer{top:4248px;height:458px;background:#000;color:#fff}
.site-footer>svg{position:absolute;left:0;top:0}
.footer-brand{position:absolute;left:128px;top:178px;display:flex;flex-direction:column;align-items:center;gap:12px;width:180px;font-family:"Oswald",Arial,sans-serif;font-weight:600;font-size:22px;color:var(--red);text-transform:uppercase;text-align:center;line-height:1.2}
.footer-brand .brand-dot{width:40px;height:40px}
.foot-col{position:absolute;top:134px}
.foot-col h6{font-family:"Oswald",Arial,sans-serif;font-weight:500;font-size:16px;text-transform:uppercase;margin-bottom:14px}
.foot-col h6 em{font-style:normal;color:var(--red)}
.foot-col li{list-style:none;font-size:14px;line-height:26px;padding-left:26px;position:relative}
.foot-col li::before{content:"»";position:absolute;left:0;top:-1px}
.contact li{padding-left:26px;line-height:26px;margin-bottom:12px}
.contact li::before{content:none}
.contact svg{position:absolute;left:0;top:6px}
.foot-rule{position:absolute;left:113px;top:362px;width:974px;height:1px;background:#3a3a3a}
.copyright{position:absolute;top:385px;width:100%;text-align:center;font-size:12px;font-weight:600}
.copyright em{font-style:normal;color:var(--red);font-weight:400}
</style>
</head>
<body>
<div class="canvas">

  <header class="block site-header">
    <a class="brand" href="#"><span class="brand-dot"></span>Kestrel Dune Pictures</a>
    <nav class="nav">
      <a class="active" href="#" style="left:366px">Home</a>
      <a href="#" style="left:448px">Commercials</a>
      <a href="#" style="left:579px">Films</a>
      <a href="#" style="left:660px">Television</a>
      <a href="#" style="left:771px">Contact</a>
    </nav>
    <div class="call">
      <span class="call-icon"><svg width="22" height="22" viewBox="0 0 24 24"><path fill="#fff" d="M6.6 10.8a15.1 15.1 0 0 0 6.6 6.6l2.2-2.2c.3-.3.7-.4 1-.2 1.1.4 2.3.6 3.6.6.6 0 1 .4 1 1V20c0 .6-.4 1-1 1A17 17 0 0 1 3 4c0-.6.4-1 1-1h3.5c.6 0 1 .4 1 1 0 1.3.2 2.5.6 3.6.1.3 0 .7-.2 1z"/></svg></span>
      <div><small>Call Us Today</small><strong>+27 82 555 0142</strong></div>
    </div>
  </header>

  <section class="block hero">
    <div class="hero-photo" role="img" aria-label="Film crew silhouetted on a studio set under production lights"></div>
    <svg class="hero-cut" width="1200" height="638" viewBox="0 0 1200 638">
      <polygon points="0,541 1200,622 1200,638 0,601" fill="#ec1f27"/>
      <polygon points="0,601 1200,638 0,638" fill="#fff"/>
    </svg>
    <div class="slide-nav prev">P<br>R<br>E<br>V</div>
    <div class="slide-nav next">N<br>E<br>X<br>T</div>
    <h1 class="hero-title">Lorem ipsum dolor sit amet</h1>
    <p class="hero-lead">Lorem ipsum dolor sit amet, consectetur adipiscing elit, sed do eiusmod<br>tempor incididunt ut labore et dolore magna aliqua.</p>
    <a class="btn btn-red" href="#">Get Started</a>
  </section>

  <section class="block about">
    <h2 class="heading">About <em>Kestrel Dune</em><span class="rule"></span></h2>
    <p>Lorem ipsum dolor sit amet, consectetur adipiscing elit, sed do eiusmod tempor incididunt ut labore et dolore magna aliqua. Ut enim ad minim veniam, quis nostrud exercitation ullamco laboris nisi ut aliquip ex ea commodo consequat. Duis aute irure dolor in reprehenderit in voluptate velit esse cillum dolore eu fugiat nulla pariatur. Excepteur sint occaecat cupidatat non proident, sunt in culpa qui officia deserunt mollit anim id est laborum.</p>
    <a class="btn btn-red" href="#">Learn More</a>
  </section>

  <section class="block services">
    <svg width="1200" height="494" viewBox="0 0 1200 494">
      <defs>
        <linearGradient id="redPanel" x1="0" y1="0" x2="1" y2="1">
          <stop offset="0" stop-color="#b40f17"/><stop offset=".6" stop-color="#e01c24"/><stop offset="1" stop-color="#ec1f27"/>
        </linearGradient>
        <linearGradient id="darkPanel" x1="0" y1="0" x2="1" y2="1">
          <stop offset="0" stop-color="#1c1c1e"/><stop offset="1" stop-color="#3c3c3f"/>
        </linearGradient>
      </defs>
      <polygon points="0,0 600,60 600,442 0,494" fill="url(#redPanel)" role="img" aria-label="Red-toned film projector backdrop"/>
      <polygon points="600,60 1200,0 1200,494 600,442" fill="url(#darkPanel)" role="img" aria-label="Dark-toned clapperboard backdrop"/>
    </svg>
    <div class="service production">
      <h3>Film Production Service</h3>
      <p>Lorem ipsum dolor sit amet, consectetur adipiscing elit, sed do eiusmod tempor incididunt ut labore et dolore magna aliqua. Ut enim ad minim veniam, quis nostrud exercitation ullamco laboris nisi.</p>
      <a class="btn btn-white" href="#">Learn More</a>
    </div>
    <div class="service development">
      <h3>We create and conceptualise our<br>own films and TV shows</h3>
      <p style="margin-top:2px">Lorem ipsum dolor sit amet, consectetur adipiscing elit, sed do eiusmod tempor incididunt ut labore et dolore magna aliqua. Ut enim ad minim veniam, quis nostrud exercitation ullamco laboris nisi.</p>
      <a class="btn btn-white" href="#">Learn More</a>
    </div>
  </section>

  <section class="block what">
    <h2 class="heading">What <em>We Do</em><span class="rule"></span></h2>

    <span class="step-num" style="left:88px;top:272px;font-size:200px">1</span>
    <div class="step" style="left:154px;top:259px">
      <svg width="90" height="80" viewBox="0 0 90 80" style="left:38px;top:-48px">
        <rect x="4" y="22" width="52" height="54" fill="#fff" stroke="#000" stroke-width="4"/>
        <rect x="4" y="22" width="12" height="54" fill="#000"/>
        <line x1="16" y1="49" x2="56" y2="49" stroke="#000" stroke-width="3"/>
        <circle cx="22" cy="12" r="9" fill="none" stroke="#000" stroke-width="4"/>
        <circle cx="44" cy="12" r="9" fill="none" stroke="#000" stroke-width="4"/>
        <polygon points="56,34 84,20 84,62 56,52" fill="#000"/>
      </svg>
      <h4 style="left:48px;top:60px">Commercials</h4>
      <p style="left:48px;top:102px">consectetur adipiscing e lit, sed do eiusmod te mpor incididunt</p>
    </div>
    <span class="step-arrow" style="left:379px;top:357px"><svg width="12" height="12" viewBox="0 0 12 12"><path d="M4 2l4 4-4 4" fill="none" stroke="#000" stroke-width="2"/></svg></span>

    <span class="step-num" style="left:428px;top:218px;font-size:200px">2</span>
    <div class="step" style="left:497px;top:205px">
      <svg width="80" height="76" viewBox="0 0 80 76" style="left:42px;top:-14px">
        <polygon points="4,20 72,6 74,16 6,30" fill="#fff" stroke="#000" stroke-width="4"/>
        <rect x="6" y="30" width="68" height="42" fill="#fff" stroke="#000" stroke-width="4"/>
        <line x1="6" y1="44" x2="74" y2="44" stroke="#000" stroke-width="4"/>
        <line x1="22" y1="30" x2="16" y2="44" stroke="#000" stroke-width="4"/>
        <line x1="40" y1="30" x2="34" y2="44" stroke="#000" stroke-width="4"/>
        <line x1="58" y1="30" x2="52" y2="44" stroke="#000" stroke-width="4"/>
      </svg>
      <h4 style="left:50px;top:104px">Films</h4>
      <p style="left:50px;top:142px">consectetur adipiscing e lit, sed do eiusmod te mpor incididunt</p>
    </div>
    <span class="step-arrow" style="left:723px;top:304px"><svg width="12" height="12" viewBox="0 0 12 12"><path d="M4 2l4 4-4 4" fill="none" stroke="#000" stroke-width="2"/></svg></span>

    <span class="step-num" style="left:768px;top:272px;font-size:200px">3</span>
    <div class="step" style="left:840px;top:258px">
      <svg width="90" height="70" viewBox="0 0 90 70" style="left:44px;top:28px">
        <rect x="4" y="4" width="82" height="46" fill="#fff" stroke="#000" stroke-width="4"/>
        <line x1="4" y1="40" x2="86" y2="40" stroke="#000" stroke-width="3"/>
        <circle cx="45" cy="22" r="11" fill="none" stroke="#000" stroke-width="3"/>
        <polygon points="42,16 51,22 42,28" fill="#000"/>
        <line x1="45" y1="50" x2="45" y2="60" stroke="#000" stroke-width="4"/>
        <line x1="24" y1="62" x2="66" y2="62" stroke="#000" stroke-width="4"/>
      </svg>
      <h4 style="left:50px;top:112px">Television</h4>
      <p style="left:50px;top:154px">consectetur adipiscing e lit, sed do eiusmod te mpor incididunt</p>
    </div>
  </section>

  <section class="block shows">
    <svg width="1200" height="831" viewBox="0 0 1200 831">
      <defs>
        <linearGradient id="showsRed" x1="0" y1="0" x2="1" y2="0">
          <stop offset="0" stop-color="#c4121a"/><stop offset="1" stop-color="#ec1f27"/>
        </linearGradient>
      </defs>
      <rect x="0" y="0" width="1200" height="831" fill="#fff"/>
      <polygon points="0,0 1200,36 1200,831 0,831" fill="#2a2a2c"/>
      <polygon points="0,0 1200,36 700,36 1200,96 1200,800 0,738" fill="url(#showsRed)"/>
    </svg>
    <h2 class="heading">Our Latest Movies &amp; TV Shows<span class="rule"></span></h2>
    <div class="show" style="left:113px">
      <span class="poster" role="img" aria-label="Movie poster: desert war drama with a soldier's portrait" style="background:linear-gradient(180deg,#3a2414 0%,#7a4a22 45%,#c98a4a 80%,#e8b98a 100%)"></span>
      <h5>Lorem ipsum dolor</h5><span>Lorem ipsum dolor sit amet</span>
    </div>
    <div class="show" style="left:361px">
      <span class="poster" role="img" aria-label="Movie poster: adventure comedy with an explorer on a yellow backdrop" style="background:linear-gradient(180deg,#5aa8d8 0%,#e0b640 45%,#d08a20 100%)"></span>
      <h5>Lorem ipsum dolor</h5><span>Lorem ipsum dolor sit amet</span>
    </div>
    <div class="show" style="left:609px">
      <span class="poster" role="img" aria-label="Movie poster: two figures silhouetted in a golden desert" style="background:linear-gradient(180deg,#2e2212 0%,#8a5a1c 40%,#d89a3a 70%,#5a3810 100%)"></span>
      <h5>Lorem ipsum dolor</h5><span>Lorem ipsum dolor sit amet</span>
    </div>
    <div class="show" style="left:857px">
      <span class="poster" role="img" aria-label="Movie poster: suited lead character in a dark red-lit city" style="background:linear-gradient(180deg,#2a2426 0%,#5a3a3a 40%,#1a1a1c 100%)"></span>
      <h5>Lorem ipsum dolor</h5><span>Lorem ipsum dolor sit amet</span>
    </div>
    <div class="dots"><i class="off"></i><i></i><i></i><i></i></div>
  </section>

  <section class="block testimonials">
    <h2 class="heading">Client <em>Testimonials</em><span class="rule"></span></h2>
    <span class="quote-mark">“</span>
    <p>Lorem ipsum dolor sit amet, consectetur adipiscing elit, sed do eiusmod tempor incididunt ut labore et dolore magna aliqua. Ut enim ad minim veniam, quis nostrud exercitation ullamco laboris nisi ut aliquip ex ea commodo consequat. Duis aute irure dolor in reprehenderit in voluptate velit esse cillum dolore t amet, consectetur, adipisci velit, sed quia non numquam eius modi tempora incidunt ut labore et dolore magnam aliquam quaerat voluptatem.</p>
    <div class="reviewer"><span class="avatar" role="img" aria-label="Client portrait"></span><span>John Deo</span></div>
  </section>

  <section class="block blogs">
    <h2 class="heading">Our <em>Latest Blogs</em><span class="rule"></span></h2>
    <article class="post" style="left:113px">
      <span class="post-photo" role="img" aria-label="Camera operator filming an actress on set" style="background:linear-gradient(135deg,#2a2a2a,#6a5a52 55%,#a04848)"></span>
      <h6>Lorem ipsum dolor sit amet, conse ctetur adipiscing elit, sed.</h6>
      <p>Lorem ipsum dolor sit amet, consectetur adipiscing elit, sed do eiusmod tempor incididunt ut.</p>
    </article>
    <article class="post" style="left:444px">
      <span class="post-photo" role="img" aria-label="Film crew with a clapperboard in a studio" style="background:linear-gradient(135deg,#1e1e1e,#5a5a5a 50%,#b8b8b8)"></span>
      <h6>Lorem ipsum dolor sit amet, conse ctetur adipiscing elit, sed.</h6>
      <p>Lorem ipsum dolor sit amet, consectetur adipiscing elit, sed do eiusmod tempor incididunt ut.</p>
    </article>
    <article class="post" style="left:775px">
      <span class="post-photo" role="img" aria-label="Professional cinema camera on set" style="background:linear-gradient(135deg,#3a3a3a,#8a8a8a 50%,#2a2a2a)"></span>
      <h6>Lorem ipsum dolor sit amet, conse ctetur adipiscing elit, sed.</h6>
      <p>Lorem ipsum dolor sit amet, consectetur adipiscing elit, sed do eiusmod tempor incididunt ut.</p>
    </article>
  </section>

  <footer class="block site-footer">
    <svg width="1200" height="80" viewBox="0 0 1200 80">
      <polygon points="0,0 1200,0 1200,20 0,0" fill="#fff"/>
      <polygon points="260,38 1200,40 1200,82" fill="#ec1f27"/>
    </svg>
    <div class="footer-brand"><span class="brand-dot"></span>Kestrel Dune Pictures</div>
    <div class="foot-col" style="left:448px">
      <h6><em>Quick</em> Links</h6>
      <ul><li>Home</li><li>Commercials</li><li>Films</li><li>Television</li><li>Contact</li></ul>
    </div>
    <div class="foot-col" style="left:661px">
      <h6><em>Follow</em> To Us</h6>
      <ul><li>Frameline</li><li>Snapreel</li><li>Clipstream</li><li>Chirper</li></ul>
    </div>
    <div class="foot-col contact" style="left:892px">
      <h6><em>Contact</em> Info</h6>
      <ul>
        <li><svg width="12" height="14" viewBox="0 0 12 14"><path fill="#ec1f27" d="M6 0a5 5 0 0 0-5 5c0 4 5 9 5 9s5-5 5-9a5 5 0 0 0-5-5zm0 7a2 2 0 1 1 0-4 2 2 0 0 1 0 4z"/></svg>Lorem ipsum dolor sit<br>amet, consectetur</li>
        <li><svg width="13" height="13" viewBox="0 0 24 24"><path fill="#ec1f27" d="M6.6 10.8a15.1 15.1 0 0 0 6.6 6.6l2.2-2.2c.3-.3.7-.4 1-.2 1.1.4 2.3.6 3.6.6.6 0 1 .4 1 1V20c0 .6-.4 1-1 1A17 17 0 0 1 3 4c0-.6.4-1 1-1h3.5c.6 0 1 .4 1 1 0 1.3.2 2.5.6 3.6.1.3 0 .7-.2 1z"/></svg>+27(0) 21 555 0186</li>
        <li><svg width="14" height="11" viewBox="0 0 14 11"><rect width="14" height="11" rx="1" fill="#ec1f27"/><path d="M1 1l6 5 6-5" fill="none" stroke="#000" stroke-width="1.4"/></svg>info@kdpictures.co.za</li>
      </ul>
    </div>
    <div class="foot-rule"></div>
    <p class="copyright">© Copyrights 2020 <em>Kestrel Dune Pictures</em> &nbsp;&nbsp; | &nbsp;&nbsp; All Rights Reserved</p>
  </footer>

</div>
</body>
</html>
```